Display Home Banner WRB

Design a Display Home Banner to go on Fence at Display Home.

Banner will need to display company logo and name.

Prefer the entire banner to be approx 6m in length and approx 1.2m high

Must also have the words "Display Home"

Specialising in unique custom built homes, knock down and rebuild

The rest is up to you to give me some ideas of your own. It needs to be modern and elegant in design. We are show casing our industry leading construction work and want to draw peoples attention to the display home!

**** FURTHER UPDATE ********

Just clarifying that I am looking for a long narrow banner (not poster format)

6 metres long and 1.2 metres high .....

Doesn't have to have construction symbols on it .... can be symbols or shapes or colors or images that compliment the text etc .....

Want the building company logo to be more prominent than the words display home but want it to be clear that its a display home banner ....

I am looking for a slick crisp font .... not too blocky or playful .....

don't want reds, yellows, orange colours ......

looking for tranquil, warm soft colours and colors from the logo ....

I am looking for a very professional corporate banner .....

I will update brief and upload logo and files tonight. Sorry for the delay

Reason: Hi Sorry I have been working on another project with another company and this was left on the side. I have now finished building the display home and need the banner for exhibitions in the coming weeks. The banner needs to display the company logo and name as well as the words "Display Home" I have uploaded the logo files for you to use with your designs. It will be approximately 6m in length and the rest of the design I leave open to your creative side :) Any questions please let me know Thanks

Im not sure that the brief was read correctly by everyone?? I am look for a long narrow banner - 6 metres long and 1.2 metres high ...... (Not Poster format) I want to use peaceful tranquil colors and the colors in our logo ..... (Not Red, Yellow and Orange ..... soft warm colours please) I want a modern striking text like the one in the logo ..... Doesn't necessarily have to have construction symbols in the banner .... can just be shapes or symbols or even just areas defined by colors .... has to look corporate and modern with a professional industry leading look to it ..... Hope this helps ! :) Looking forward to seeing some updated concepts! :) Thanks!

Target Market(s)

People looking for a quality builder to build for them.

Industry/Entity Type

Construction

```html
<!DOCTYPE html>
<html lang="en">
<head>
<meta charset="utf-8">
<title>Display Home Banner – WRB Homes</title>
<link rel="stylesheet" href="https://fonts.googleapis.com/css2?family=Jost:wght@500;700&display=swap">
<style>
  :root {
    --canvas-top: #e6e6e6;
    --canvas-mid: #f7f7f7;
    --white: #ffffff;

    --blue-pattern-a: #1aa6dc;
    --blue-pattern-b: #0a6fa8;
    --green-a: #5cb843;
    --green-b: #b3d432;
    --blue-brand: #0b95cc;
    --blue-brand-light: #2fb1e0;

    --purple-pattern-a: #a0549e;
    --purple-pattern-b: #6c2a7a;
    --pink-a: #e4306a;
    --pink-b: #e2386f;
    --plum-brand: #4b0a47;
    --plum-brand-light: #5e1559;

    --rose-pattern-a: #d8445a;
    --rose-pattern-b: #8a2a6a;
    --violet-a: #6a2a82;
    --violet-b: #a0237e;
    --wine-brand: #7a1c50;
    --wine-brand-light: #8a2660;
  }

  * { box-sizing: border-box; margin: 0; padding: 0; }

  html, body {
    width: 1200px;
    height: 1000px;
    overflow: hidden;
  }

  body {
    position: relative;
    background: linear-gradient(180deg, var(--canvas-top) 0%, var(--canvas-mid) 45%, var(--canvas-top) 100%);
    font-family: "Jost", "Helvetica Neue", Arial, sans-serif;
    color: var(--white);
  }

  .banner {
    position: absolute;
    left: 0;
    width: 1200px;
    height: 240px;
    display: flex;
    box-shadow: 0 6px 14px rgba(0, 0, 0, 0.18);
  }
  .banner--one   { top: 92px; }
  .banner--two   { top: 375px; }
  .banner--three { top: 665px; }

  .banner__pattern {
    width: 265px;
    height: 100%;
    flex: none;
  }

  .banner__message {
    width: 599px;
    height: 100%;
    flex: none;
    display: flex;
    flex-direction: column;
    align-items: center;
    padding-top: 28px;
    box-shadow: 0 0 10px rgba(0, 0, 0, 0.25);
    position: relative;
    z-index: 1;
  }

  .banner__brand {
    flex: 1;
    height: 100%;
    display: flex;
    align-items: center;
    justify-content: center;
    gap: 16px;
  }

  .pin-icon {
    width: 58px;
    height: 80px;
    filter: drop-shadow(0 2px 3px rgba(0, 0, 0, 0.25));
  }

  .headline {
    margin-top: 14px;
    font-weight: 700;
    font-size: 40px;
    letter-spacing: 4px;
    line-height: 1;
    text-shadow: 0 2px 4px rgba(0, 0, 0, 0.3);
  }

  .tagline {
    margin-top: 8px;
    font-weight: 700;
    font-size: 11.5px;
    letter-spacing: 0.3px;
    text-shadow: 0 1px 2px rgba(0, 0, 0, 0.35);
  }

  .brand-square {
    width: 34px;
    height: 34px;
    background: var(--white);
  }

  .brand-name {
    font-weight: 500;
    font-size: 34px;
    letter-spacing: 3px;
    line-height: 1;
  }

  /* Row 1 – blue & green */
  .banner--one .banner__pattern {
    background: linear-gradient(120deg, var(--blue-pattern-a), var(--blue-pattern-b));
  }
  .banner--one .banner__message {
    background: radial-gradient(circle at 65% 35%, var(--green-b) 0%, var(--green-a) 100%);
  }
  .banner--one .banner__brand {
    background: radial-gradient(circle at 40% 20%, var(--blue-brand-light), var(--blue-brand) 70%);
  }

  /* Row 2 – violet & pink */
  .banner--two .banner__pattern {
    background: linear-gradient(120deg, var(--purple-pattern-a), var(--purple-pattern-b));
  }
  .banner--two .banner__message {
    background: linear-gradient(90deg, var(--pink-a), var(--pink-b));
  }
  .banner--two .banner__brand {
    background: radial-gradient(circle at 40% 30%, var(--plum-brand-light), var(--plum-brand) 75%);
  }

  /* Row 3 – rose & violet */
  .banner--three .banner__pattern {
    background: linear-gradient(160deg, var(--rose-pattern-a), var(--rose-pattern-b));
  }
  .banner--three .banner__message {
    background: linear-gradient(100deg, var(--violet-a), var(--violet-b));
  }
  .banner--three .banner__brand {
    background: radial-gradient(circle at 40% 30%, var(--wine-brand-light), var(--wine-brand) 75%);
  }
</style>
</head>
<body>

  <section class="banner banner--one">
    <div class="banner__pattern" role="img" aria-label="Geometric triangle pattern with connected lines and small location icons in blue"></div>
    <div class="banner__message">
      <svg class="pin-icon" viewBox="0 0 58 80" aria-hidden="true">
        <path d="M29 2C14 2 2 14 2 29c0 20 27 49 27 49s27-29 27-49C56 14 44 2 29 2z" fill="#fff"/>
        <circle cx="29" cy="28" r="16" fill="none" stroke="#6cbf3e" stroke-width="3"/>
      </svg>
      <h1 class="headline">DISPLAY HOME</h1>
      <p class="tagline">SPECIALISING IN KNOCK DOWN AND REBUILD, UNIQUE CUSTOM BUILT HOMES</p>
    </div>
    <div class="banner__brand">
      <span class="brand-square"></span>
      <span class="brand-name">WRB HOMES</span>
    </div>
  </section>

  <section class="banner banner--two">
    <div class="banner__pattern" role="img" aria-label="Geometric triangle pattern with connected lines and small location icons in purple"></div>
    <div class="banner__message">
      <svg class="pin-icon" viewBox="0 0 58 80" aria-hidden="true">
        <path d="M29 2C14 2 2 14 2 29c0 20 27 49 27 49s27-29 27-49C56 14 44 2 29 2z" fill="#fff"/>
        <circle cx="29" cy="28" r="16" fill="none" stroke="#e2336c" stroke-width="3"/>
      </svg>
      <h1 class="headline">DISPLAY HOME</h1>
      <p class="tagline">SPECIALISING IN KNOCK DOWN AND REBUILD, UNIQUE CUSTOM BUILT HOMES</p>
    </div>
    <div class="banner__brand">
      <span class="brand-square"></span>
      <span class="brand-name">WRB HOMES</span>
    </div>
  </section>

  <section class="banner banner--three">
    <div class="banner__pattern" role="img" aria-label="Geometric triangle pattern with connected lines and small location icons in rose and plum"></div>
    <div class="banner__message">
      <svg class="pin-icon" viewBox="0 0 58 80" aria-hidden="true">
        <path d="M29 2C14 2 2 14 2 29c0 20 27 49 27 49s27-29 27-49C56 14 44 2 29 2z" fill="#fff"/>
        <circle cx="29" cy="28" r="16" fill="none" stroke="#8a2680" stroke-width="3"/>
      </svg>
      <h1 class="headline">DISPLAY HOME</h1>
      <p class="tagline">SPECIALISING IN KNOCK DOWN AND REBUILD, UNIQUE CUSTOM BUILT HOMES</p>
    </div>
    <div class="banner__brand">
      <span class="brand-square"></span>
      <span class="brand-name">WRB HOMES</span>
    </div>
  </section>

</body>
</html>
```